Business Card Design Project

I need a cool business card design for the company that will build residential houses.
The card should include:
1) Name: Boris Kalinov
2) Cell: 587.204.XXXX
3) Email: bor.kalinov@qwvend.example
4) Position: General Manager
5) Residential Home Building
6) Company logo that I have uploaded

Industry/Entity Type

Residential

```html
<!DOCTYPE html>
<html lang="en">
<head>
<meta charset="utf-8">
<title>Veltrano Developments — Business Card</title>
<link rel="stylesheet" href="https://fonts.googleapis.com/css2?family=Open+Sans:wght@400;600;700&display=swap">
<style>
  :root {
    --bg: #ece9e4;
    --brand-blue: #1f4fa3;
    --deep-blue: #163f8c;
    --light-blue: #2a86cc;
    --brand-green: #5cb33e;
    --ink-grey: #6d6d6d;
    --rule-grey: #c4c4c4;
    --paper: #ffffff;
  }
  * { box-sizing: border-box; margin: 0; padding: 0; }
  html, body {
    width: 1200px; height: 836px; overflow: hidden;
    background: var(--bg);
    font-family: "Open Sans", Arial, sans-serif;
  }
  .stage {
    position: relative; width: 1200px; height: 836px;
  }
  .card {
    position: absolute; left: 300px;
    width: 600px; height: 343px;
    border-radius: 22px; overflow: hidden;
    box-shadow: 0 8px 24px rgba(0,0,0,0.18);
  }
  .card-front { top: 48px; background: var(--paper); }
  .card-back {
    top: 445px;
    background: radial-gradient(ellipse at 48% 40%, var(--light-blue) 0%, var(--brand-blue) 62%, var(--deep-blue) 100%);
  }
  .card-art { position: absolute; inset: 0; width: 100%; height: 100%; }

  .front-brand {
    position: absolute; right: 52px; top: 96px; text-align: right;
  }
  .brand-mark {
    display: flex; align-items: center; justify-content: flex-end; gap: 8px;
  }
  .brand-dot {
    width: 14px; height: 14px; border-radius: 50%; background: var(--brand-green);
  }
  .brand-name {
    font-weight: 700; font-size: 25px; letter-spacing: 0.5px; color: var(--brand-blue);
    line-height: 1;
  }
  .brand-tagline {
    margin-top: 10px; font-size: 15px; font-weight: 600; color: var(--brand-green);
  }
  .front-rule {
    position: absolute; left: 78px; right: 52px; top: 186px;
    height: 1px; background: var(--rule-grey);
  }
  .contact {
    position: absolute; left: 78px; top: 196px;
  }
  .contact-name { font-size: 15px; color: var(--ink-grey); }
  .contact-name strong { font-weight: 600; color: var(--brand-blue); }
  .contact-line {
    display: flex; align-items: center; gap: 8px;
    margin-top: 5px; font-size: 13px; color: var(--ink-grey);
  }
  .contact-line svg { width: 12px; height: 12px; flex: none; }

  .back-brand {
    position: absolute; left: 0; right: 0; top: 128px;
    display: flex; align-items: center; justify-content: center; gap: 10px;
  }
  .back-brand .brand-name { color: var(--paper); font-size: 30px; }
  .back-brand .brand-dot { width: 16px; height: 16px; background: var(--paper); }
  .back-url {
    position: absolute; left: 0; right: 0; bottom: 44px;
    text-align: center; font-size: 14px; color: var(--paper);
  }
</style>
</head>
<body>
<main class="stage">
  <section class="card card-front" aria-label="Card front">
    <svg class="card-art" viewBox="0 0 600 343" preserveAspectRatio="none" aria-hidden="true">
      <path d="M0,0 H600 V22 Q300,16 0,120 Z" fill="var(--brand-blue)"/>
      <path d="M0,128 Q300,26 600,30" fill="none" stroke="var(--brand-green)" stroke-width="5"/>
      <path d="M0,343 H600 V222 Q330,322 0,318 Z" fill="var(--brand-blue)"/>
      <path d="M0,306 Q330,312 600,212" fill="none" stroke="var(--brand-green)" stroke-width="5"/>
    </svg>
    <div class="front-brand">
      <div class="brand-mark">
        <span class="brand-dot"></span>
        <span class="brand-name">VELTRANO Developments</span>
      </div>
      <p class="brand-tagline">Residential Home Building</p>
    </div>
    <div class="front-rule"></div>
    <div class="contact">
      <p class="contact-name"><strong>Boris Kalinov</strong> General Manager</p>
      <p class="contact-line">
        <svg viewBox="0 0 12 12"><rect x="3" y="0.5" width="6" height="11" rx="1.2" fill="none" stroke="var(--brand-blue)" stroke-width="1.2"/><circle cx="6" cy="9.5" r="0.7" fill="var(--brand-blue)"/></svg>
        587.204.XXXX
      </p>
      <p class="contact-line">
        <svg viewBox="0 0 12 12"><rect x="0.6" y="2.5" width="10.8" height="7.5" fill="none" stroke="var(--brand-blue)" stroke-width="1.2"/><path d="M0.6,2.5 L6,7 L11.4,2.5" fill="none" stroke="var(--brand-blue)" stroke-width="1.2"/></svg>
        bor.kalinov@qwvend.example
      </p>
    </div>
  </section>

  <section class="card card-back" aria-label="Card back">
    <div class="back-brand">
      <span class="brand-dot"></span>
      <span class="brand-name">VELTRANO Developments</span>
    </div>
    <p class="back-url">www.veltranohomes.example</p>
  </section>
</main>
</body>
</html>
```